Magician | Speaker looks for an innovative business card design

I'm a magician and public speaker offering artistic and modern magical experiences.
I'm based in Brussels (Belgium.) I love magic performed up-close, creating a space of intimacy, even when I'm on stage.
The final design should communicate professionalism, elegance, artistry, and a friendly kind personality

I would like to see designs based either on my photos and/or the way I sign my name Remy Vok (see attached files for more info.)
Additional photos and more info about what I offer can be seen at www.remy-vok.net

My current business card design is also attached. I like the fact that the reverse of my current design includes quotes from master magicians about magic, changing the way my participants see the art of magic.

Note: I would like a double-sided card design. However, I need white space on the reverse to be able to write things on for my performances.

Details to include on the card:
Artist name: Remy Vok
Offer: magician + (public) speaker or magic + (public) speaking (the + sign can be replaced by another character, like a bullet or a pipe)
Phone: +32 471 265 903
Email: book@remy-vok.net
(optional) Website: www.remy-vok.net or remy-vok.net

Target Market(s)

Corporate, organisations, companies as well as individuals

Industry/Entity Type

Artists

Colors

Designer to choose colors to be used in the design.

Requirements
Nice to have
• A side with a mirror could be nice

```html
<!DOCTYPE html>
<html lang="en">
<head>
<meta charset="utf-8">
<title>Remy Vok – Magician &amp; Public Speaker – Card Backs</title>
<link rel="stylesheet" href="https://fonts.googleapis.com/css2?family=Lato:wght@700;900&display=swap">
<style>
  :root {
    --cream: #e4dacb;
    --name: #efe8db;

    --ruby-bg: #2b0709;
    --ruby-deep: #160304;
    --ruby-line: #b2343b;
    --ruby-glow: rgba(190, 50, 58, 0.42);

    --ash-bg: #201b1a;
    --ash-deep: #0f0c0c;
    --ash-line: #8f8782;
    --ash-glow: rgba(150, 140, 135, 0.30);

    --teal-bg: #0b2022;
    --teal-deep: #050f10;
    --teal-line: #1e8ea1;
    --teal-glow: rgba(30, 140, 160, 0.40);
  }

  * { box-sizing: border-box; margin: 0; padding: 0; }

  html, body {
    width: 1200px;
    height: 666px;
    overflow: hidden;
    background: #0d0a0a;
  }

  .card-set {
    display: flex;
    width: 1200px;
    height: 666px;
  }

  .card {
    position: relative;
    width: 400px;
    height: 666px;
    background: radial-gradient(ellipse at 50% 50%, var(--bg) 0%, var(--deep) 100%);
    font-family: "Lato", sans-serif;
    overflow: hidden;
  }

  .card--ruby { --bg: var(--ruby-bg); --deep: var(--ruby-deep); --line: var(--ruby-line); --glow: var(--ruby-glow); }
  .card--ash  { --bg: var(--ash-bg);  --deep: var(--ash-deep);  --line: var(--ash-line);  --glow: var(--ash-glow); }
  .card--teal { --bg: var(--teal-bg); --deep: var(--teal-deep); --line: var(--teal-line); --glow: var(--teal-glow); }

  .card__frame {
    position: absolute;
    left: 32px;
    top: 30px;
    width: 336px;
    height: 604px;
    border: 1.5px solid var(--line);
    border-radius: 16px;
  }

  .card__emblem {
    position: absolute;
    left: 50px;
    top: 45px;
    width: 300px;
    height: 585px;
    background:
      radial-gradient(circle at 50% 50%, var(--glow) 0%, transparent 32%),
      radial-gradient(circle at 50% 17%, var(--glow) 0%, transparent 22%),
      radial-gradient(circle at 50% 85%, var(--glow) 0%, transparent 22%);
    opacity: 0.8;
  }

  .card__role {
    position: absolute;
    left: 0;
    width: 100%;
    text-align: center;
    color: var(--cream);
    font-weight: 900;
    letter-spacing: 0.12em;
    line-height: 1;
  }

  .card__role--top { top: 136px; font-size: 27px; }
  .card__role--small { top: 488px; font-size: 21px; font-weight: 700; letter-spacing: 0.1em; }
  .card__role--bottom { top: 508px; font-size: 29px; letter-spacing: 0.16em; }

  .card__name {
    position: absolute;
    left: 0;
    top: 308px;
    width: 100%;
    text-align: center;
    color: var(--name);
    font-size: 54px;
    font-weight: 900;
    line-height: 1;
  }
</style>
</head>
<body>
  <main class="card-set">
    <section class="card card--ruby">
      <div class="card__emblem" role="img" aria-label="Geometric magic circle emblem in red line work"></div>
      <div class="card__frame"></div>
      <p class="card__role card__role--top">MAGICIAN</p>
      <p class="card__name">Remy Vok</p>
      <p class="card__role card__role--small">PUBLIC</p>
      <p class="card__role card__role--bottom">SPEAKER</p>
    </section>

    <section class="card card--ash">
      <div class="card__emblem" role="img" aria-label="Geometric magic circle emblem in grey line work"></div>
      <div class="card__frame"></div>
      <p class="card__role card__role--top">MAGICIAN</p>
      <p class="card__name">Remy Vok</p>
      <p class="card__role card__role--small">PUBLIC</p>
      <p class="card__role card__role--bottom">SPEAKER</p>
    </section>

    <section class="card card--teal">
      <div class="card__emblem" role="img" aria-label="Geometric magic circle emblem in teal line work"></div>
      <div class="card__frame"></div>
      <p class="card__role card__role--top">MAGICIAN</p>
      <p class="card__name">Remy Vok</p>
      <p class="card__role card__role--small">PUBLIC</p>
      <p class="card__role card__role--bottom">SPEAKER</p>
    </section>
  </main>
</body>
</html>
```